Remote Game Console (Rexlet) Wpf/Web UI

A complete interface for a second generation remote console tool to administer PC games. Will primarily run as a desktop application with future plans of running within a browser.

All materials are supplied as a guide only, but the designer is free to build what they would find easy to use. We're engineers so help us out with a good user experience.

The first version of Rexlet Hailcore was released in March 2009 supporting Skirmline: Iron Squad 2. It was updated later in the year to support the expansion, SLIS2: Vietnam. Crest of Valor followed in late 2010 and Skirmline 3 support in October 2011. All games are based on KORU's Hailcore engine. http://quimbly.net/rexlet-hailcore/

Rexlet 2 will eventually support all games, working more along the lines of a framework for others to expand upon. While ultimately having a similar function as Rexlet Hailcore, Rexlet 2 has been completely rewritten and shares no similarities internally.

The primary focus of the application is to display details about a users rented Game Server. A user can kick, ban and chat with players in their servers. A user can alter the settings of their game server, setting the time of a round or the game servers name for instance.

We have a forum dedicated to this competition that users of our software can give general feedback about the existing (Rexlet Hailcore) software, such as what they hate etc. http://www.quimbly.net/forumvb/forumdisplay.php?35-UI-Competition

You can find similar software with much cooler looking UI's at http://www.sl2hq.com/ and http://sl3hq.com/

The techy details:

Rexlet 2 can run locally or connect and login to a hosted version of the software (internally we call this a Local Interface or Remote Interface). Logging into a remote server requires an IP, port, username and password. Beyond the initial local/remote selection the UI can function identically.

1 Instance of the software has a single Local (no login required) or Remote (ip/port/username/password required) Interface.

1 Instance has many Packages. A package is an extension to the software that the user can install. A package can be an update to Rexlet 2 itself, a plugin or a config.

1 Instance has many Options. We are partial to Zentix Lumas Options panel. Something similar which would allow us to expand would be neat.

1 Instance has many languages.

1 Interface has many Game Connections. A game connection requires an ip, port and password to connect and authenticate. A game connection has a name, maximum players allowed to connect, a game type (e.g iron squad 2, crest of valor, skirmline 3).

1 Game Connection has many plugins. A plugin extends the functionality of the software in the background.

1 Game Connection has many players. A player has a name, country, score, ping, kills, deaths and other variables depending on the type of Game connected to.

1 Game Connection has many bans. A ban is a record of a player, the players identifying information, a small description of why the ban was put in place as well as an expiry time (e.g. banned for 2 weeks or permanently banned)

1 Game Connection has many settings. These settings can vary dramatically depending on the Game connected to.

1 Interface has many Groups. A group has a name any many permissions.

1 Group has many Accounts.

1 Account has many players.

Project Deadline Extended
Reason: Uploaded wireframes. I work a lot and this is my side project. I thought I would have wireframes the next day of this project, but it didn't end up like that. All current submissions have been the first iteration of my software reskinned, not the next version.

First Person Shooter PC game administrators

Software

• Rexlet 2 has a primitive natural language parser for converting free text into commands for the program. An online functional example is available at http://labs.tevani.com.au/the-cheap-vela/ (check down the bottom). The design should incorporate a text box throughout the application for users to enter commands in. As the user types this could be passed to display what will happen once the user executes the command

Generally people will be minimizing their games to kick or ban people from their servers. The UI design should be easy enough to navigate quickly.

A UI that can handle multiple languages. Our primary market is Germany.

The UI must be usable at 1024x768. It should be designed to take up the maximum window/browser space.
• Responsive design that scales to any resolution. We have a large mobile user base that could benefit from a UI that scales well on lower resolutions.

Rexlet 2 has no set logo as of yet, though we will continue using the smiley found at http://quimbly.net - we only have a 100 by 100px png of this image though. If a larger version is supplied you'll receive a virtual cookie and a thank you! The logo will probably end up as a variation of that found on http://quimbly.net/rexlet-hailcore/ but we'll go through the exact process for this at a later date

```html
<!DOCTYPE html>
<html lang="en">
<head>
<meta charset="utf-8">
<title>Rexlet 2 — Login</title>
<link rel="stylesheet" href="https://fonts.googleapis.com/css2?family=Signika:wght@600&family=Arimo:wght@400&display=swap">
<style>
  :root {
    --bg: #21232b;
    --accent: #f7a21b;
    --white: #ffffff;
    --ink: #1b1b1b;
    --field: #000000;
    --field-text: #7d7d7d;
    --panel-top: #f7f7f7;
    --panel-bottom: #d6d6d6;
    --bar-dark: #101317;
    --bar-teal: #1c5a6e;
    --scene-sky: #5f7686;
    --scene-mid: #3b4650;
    --scene-dark: #1c2026;
  }
  * { box-sizing: border-box; margin: 0; padding: 0; }
  html, body { width: 1200px; height: 720px; overflow: hidden; background: var(--bg); }
  .canvas { position: relative; width: 1200px; height: 720px; overflow: hidden; background: var(--bg); font-family: "Arimo", Arial, sans-serif; }

  .hero-scene {
    position: absolute; left: 560px; top: 0; width: 640px; height: 720px;
    background:
      radial-gradient(ellipse 60% 45% at 70% 30%, rgba(150,170,180,.55), transparent 70%),
      radial-gradient(ellipse 55% 55% at 62% 62%, rgba(70,72,62,.7), transparent 75%),
      linear-gradient(180deg, var(--scene-sky) 0%, var(--scene-mid) 55%, var(--scene-dark) 100%);
    -webkit-mask-image: linear-gradient(90deg, transparent 0%, #000 35%);
            mask-image: linear-gradient(90deg, transparent 0%, #000 35%);
  }

  .brand { position: absolute; left: 147px; top: 328px; display: flex; align-items: center; gap: 10px; }
  .brand-dot { width: 76px; height: 76px; border-radius: 50%; background: #111; }
  .brand-name { font-family: "Signika", sans-serif; font-weight: 600; font-size: 50px; color: var(--white); letter-spacing: 1px; }

  .login-mode { position: absolute; left: 494px; top: 160px; font-family: "Signika", sans-serif; font-weight: 600; }
  .login-title { color: var(--accent); font-size: 22px; line-height: 28px; }
  .mode-option { display: flex; align-items: center; gap: 12px; margin-top: 6px; color: var(--white); font-size: 23px; line-height: 28px; }
  .radio { width: 15px; height: 15px; border-radius: 50%; background: radial-gradient(circle at 40% 35%, #fff, #cfcfcf); }

  .member-bar {
    position: absolute; left: 479px; top: 275px; width: 356px; height: 37px;
    border: 1px solid #3a3f45; border-radius: 4px;
    background: linear-gradient(90deg, var(--bar-dark) 0%, var(--bar-dark) 35%, var(--bar-teal) 70%, var(--bar-dark) 100%);
    display: flex; align-items: center; padding-left: 10px; gap: 16px;
    color: #e8e8e8; font-size: 14px;
  }
  .bar-dot { width: 28px; height: 28px; border-radius: 50%; background: #222; }

  .login-panel {
    position: absolute; left: 482px; top: 315px; width: 353px; height: 165px;
    border-radius: 5px; border: 1px solid #9a9a9a;
    background: linear-gradient(180deg, var(--panel-top), var(--panel-bottom));
  }
  .field-row { position: absolute; left: 0; width: 100%; height: 29px; display: flex; align-items: center; }
  .field-label { width: 115px; text-align: right; padding-right: 12px; font-size: 12px; color: var(--ink); }
  .field-input { width: 214px; height: 29px; border-radius: 6px; background: var(--field); color: var(--field-text); font-size: 12px; line-height: 29px; padding-left: 14px; }
  .row-ip { top: 15px; } .row-user { top: 49px; } .row-pass { top: 83px; }

  .remember { position: absolute; left: 22px; top: 127px; display: flex; align-items: center; gap: 9px; font-size: 12px; color: var(--ink); }
  .checkbox { width: 10px; height: 10px; border: 1px solid #666; background: #fff; }
  .register { position: absolute; left: 212px; top: 128px; font-size: 12px; color: var(--ink); text-decoration: underline; }
  .login-button {
    position: absolute; left: 271px; top: 117px; width: 71px; height: 30px;
    border: 1px solid #9c9c9c; border-radius: 5px;
    background: linear-gradient(180deg, #ffffff, #d2d2d2);
    font-size: 12px; color: var(--ink); text-align: center; line-height: 28px;
  }
</style>
</head>
<body>
<main class="canvas">
  <div class="hero-scene" role="img" aria-label="Photograph of a soldier in combat gear aiming a rifle against a cloudy sky"></div>

  <div class="brand">
    <span class="brand-dot"></span>
    <span class="brand-name">Rexlet 2</span>
  </div>

  <section class="login-mode">
    <h1 class="login-title">LOGIN</h1>
    <div class="mode-option"><span class="radio"></span>Personal</div>
    <div class="mode-option"><span class="radio"></span>Remote</div>
  </section>

  <div class="member-bar"><span class="bar-dot"></span><span>///&nbsp; Member Area</span></div>

  <form class="login-panel">
    <div class="field-row row-ip"><span class="field-label">Server IP</span><span class="field-input">192.168.0.22</span></div>
    <div class="field-row row-user"><span class="field-label">Username</span><span class="field-input">kestrel_17</span></div>
    <div class="field-row row-pass"><span class="field-label">Password</span><span class="field-input">***********</span></div>
    <div class="remember"><span class="checkbox"></span>Remember me</div>
    <span class="register">Register</span>
    <span class="login-button">LOGIN</span>
  </form>
</main>
</body>
</html>
```